Miss Dorrel Teen Postcard for special events

Need creative display for platform of logo for Miss Dorrel on her large postcards. Be kind, be bold, be brave, be you is the message. Please include this quote:
Kindness is the language which the deaf can hear
and the blind can see. - Hobart Lune
Her title is 2017 Miss Dorrel Hollin Starlet Teen. Her name is Corinne Vask. We have pics that we want included on the card. We want it to have a front and back. You can use any combination of the photos. thanks!

Target Market(s)

Youth/ Young Adults

Industry/Entity Type

Events

Font styles to use
Sans Serif
Script

Colors
86cfc6
33b8a4
3276b5
0255a3

Requirements
Must have
• Kindness is the language which the deaf can hear
• and the blind can see. - Hobart Lune
• Title-
• Name
• She is partial to the jumpsuit photo for the front but open to others
• Be Kind, Be Bold, Be Brave, Be you - would like this on the front
• Also please include Instgram: crvask202 twitter: crvask202 corinne47@pelvomail.net
• #kindboldbrave
Nice to have
• Anything that would inspire youth especially. Have begun events at hospitals and lining up work to assist with donations for community resources but not sure that is appropriate for this. We lean more towards the green than the blue, unless it ties with other things you see better- or a better shade.thanks
Should not have
• Should be age appropriate and appropriate for all ages.
• Postcard is for handing out / does not need to be mailed. Can seek revisions if this becomes the case

```html
<!DOCTYPE html>
<html lang="en">
<head>
<meta charset="utf-8">
<title>Corinne Vask – Postcard Front and Back</title>
<link href="https://fonts.googleapis.com/css2?family=Parisienne&family=Questrial&family=Montserrat:wght@700&display=swap" rel="stylesheet">
<style>
  :root {
    --teal: #22b8a4;
    --teal-mist: rgba(190, 232, 224, 0.78);
    --teal-line: rgba(150, 215, 205, 0.9);
    --blush: #f7c1b4;
    --brick: #a4574b;
    --white: #ffffff;
    --backdrop: #e9e6e2;
  }
  html, body {
    margin: 0;
    width: 904px;
    height: 1200px;
    overflow: hidden;
    background: var(--backdrop);
  }
  .canvas { position: relative; width: 904px; height: 1200px; }
  .postcard {
    position: absolute;
    left: 120px;
    width: 700px;
    height: 500px;
    transform: scale(0.926);
    transform-origin: top left;
    overflow: hidden;
    box-shadow: 0 3px 8px rgba(0,0,0,0.25);
    font-family: "Questrial", sans-serif;
  }
  .postcard--front { top: 85px; }
  .postcard--back { top: 613px; }
  .shapes { position: absolute; inset: 0; width: 700px; height: 500px; }
  .photo-zone { position: absolute; inset: 0; }
  .front-photo {
    background: linear-gradient(100deg, #8a9a78 0%, #cfc8c0 40%, #e9dcd2 60%, #c97e62 78%, #ddd3cc 100%);
  }
  .back-photo {
    background: linear-gradient(120deg, #6e8a58 0%, #c9a07e 20%, #e8c4ad 45%, #b78866 70%, #c9b6a8 100%);
  }
  .abs { position: absolute; }
  .line { display: block; white-space: nowrap; }

  /* Front */
  .title {
    left: 72px; top: 26px; width: 300px;
    color: var(--white); font-size: 24px; line-height: 31px; text-align: center;
  }
  .script-name {
    font-family: "Parisienne", cursive; color: var(--blush); white-space: nowrap; text-align: center;
  }
  .front-name { left: 42px; top: 110px; width: 310px; font-size: 50px; line-height: 64px; }
  .quote {
    left: 22px; top: 216px; width: 300px; text-align: center;
    color: var(--white); font-family: "Parisienne", cursive; font-size: 20px; line-height: 25px;
  }
  .quote-mark {
    position: absolute; left: -2px; top: -8px; font-size: 46px; line-height: 46px;
    color: rgba(255,255,255,0.35); font-family: Georgia, serif;
  }
  .quote-author { font-family: "Questrial", sans-serif; font-size: 15px; }
  .motto {
    left: 30px; top: 326px; width: 260px;
    color: var(--white); font-family: "Parisienne", cursive; font-size: 26px; line-height: 34px;
  }
  .motto b { font-weight: normal; color: var(--blush); }
  .motto .dot { font-family: "Questrial", sans-serif; font-size: 13px; margin: 0 8px; vertical-align: 5px; }

  /* Contact bands */
  .contact-band {
    position: absolute; left: 0; width: 700px; height: 52px;
    display: flex; align-items: center; color: var(--brick); font-size: 19px;
  }
  .postcard--front .contact-band { top: 421px; }
  .postcard--back .contact-band { top: 443px; height: 57px; }
  .contact { position: absolute; display: flex; align-items: center; gap: 6px; }
  .contact--insta { left: 40px; }
  .contact--mail { left: 238px; }
  .contact--bird { left: 536px; }
  .mark-square { width: 11px; height: 11px; background: var(--brick); }
  .mark-circle { width: 12px; height: 12px; border-radius: 50%; background: var(--brick); }

  /* Back */
  .back-name { left: 296px; top: 34px; width: 326px; font-size: 52px; line-height: 66px; }
  .story {
    left: 337px; top: 134px; width: 300px; text-align: center;
    color: var(--white); font-size: 15px; line-height: 18px;
  }
  .story-gap { display: block; height: 18px; }
  .donate-button {
    left: 423px; top: 322px; width: 247px; height: 34px; border-radius: 10px;
    background: var(--brick); color: var(--white); text-align: center; line-height: 35px;
    font-family: "Montserrat", sans-serif; font-weight: 700; font-size: 17px;
  }
  .call-to-action {
    left: 428px; top: 378px; width: 260px; text-align: center; color: var(--white);
    font-family: "Montserrat", sans-serif; font-weight: 700; font-size: 12.5px; line-height: 16.5px;
  }
</style>
</head>
<body>
<div class="canvas">

  <section class="postcard postcard--front">
    <div class="photo-zone front-photo" role="img" aria-label="Portrait photo of Corinne Vask in a rust jumpsuit on a city sidewalk"></div>
    <svg class="shapes" viewBox="0 0 700 500" aria-hidden="true">
      <polygon points="105,0 425,0 248,500 0,500 0,292" fill="var(--teal)"/>
      <rect x="0" y="421" width="700" height="52" fill="var(--teal-mist)"/>
      <rect x="0" y="421" width="700" height="4" fill="var(--teal-line)"/>
    </svg>
    <div class="abs title">2017 Miss Dorrel<br>Hollin Starlet Teen</div>
    <div class="abs script-name front-name">Corinne Vask</div>
    <div class="abs quote">
      <span class="quote-mark">“</span>
      <span class="line">Kindness is the language which</span>
      <span class="line">the deaf can hear - and the</span>
      <span class="line">blind can see”. <span class="quote-author">Hobart Lune</span></span>
    </div>
    <div class="abs motto">
      <span class="line"><b>BE</b> Kind<span class="dot">○</span><b>BE</b> Bold</span>
      <span class="line"><b>BE</b> Brave<span class="dot">○</span><b>BE</b> You</span>
    </div>
    <div class="contact-band">
      <span class="contact contact--insta"><span class="mark-square"></span>crvask202</span>
      <span class="contact contact--mail">
        <svg width="14" height="10" viewBox="0 0 14 10" aria-hidden="true"><rect width="14" height="10" fill="var(--brick)"/><polyline points="0,0 7,6 14,0" fill="none" stroke="#e6d2cc" stroke-width="1.2"/></svg>
        corinne47@pelvomail.net</span>
      <span class="contact contact--bird"><span class="mark-circle"></span>crvask202</span>
    </div>
  </section>

  <section class="postcard postcard--back">
    <div class="photo-zone back-photo" role="img" aria-label="Close-up portrait photo of Corinne Vask with hand in her curly hair, city buildings behind"></div>
    <svg class="shapes" viewBox="0 0 700 500" aria-hidden="true">
      <polygon points="270,0 595,0 700,208 700,442 435,442" fill="var(--teal)"/>
      <rect x="0" y="438" width="700" height="5" fill="#bfe6de"/>
      <rect x="0" y="443" width="700" height="57" fill="var(--blush)"/>
    </svg>
    <div class="abs script-name back-name">Corinne Vask</div>
    <div class="abs story">
      <span class="line" style="transform: translateX(12px)">Vask was named Miss Hollin Starlet</span>
      <span class="line" style="transform: translateX(19px)">Teen Dorrel at the HST Pageant on</span>
      <span class="line" style="transform: translateX(26px)">June 16-18. Separated into six differ-</span>
      <span class="line" style="transform: translateX(33px)">ent age groups, Vask won the Teen</span>
      <span class="line" style="transform: translateX(40px)">division (ages 16-18) at the pageant.</span>
      <span class="story-gap"></span>
      <span class="line" style="transform: translateX(53px)">She is doing some fundraising for</span>
      <span class="line" style="transform: translateX(60px)">community resources and visited</span>
      <span class="line" style="transform: translateX(66px)">children in the hospital.</span>
    </div>
    <div class="abs donate-button">DONATE NOW</div>
    <div class="abs call-to-action">
      <span class="line">Check your local school community</span>
      <span class="line">or church for opportunities</span>
      <span class="line">for assisting others!</span>
    </div>
    <div class="contact-band">
      <span class="contact contact--insta"><span class="mark-square"></span>crvask202</span>
      <span class="contact contact--mail">
        <svg width="14" height="10" viewBox="0 0 14 10" aria-hidden="true"><rect width="14" height="10" fill="var(--brick)"/><polyline points="0,0 7,6 14,0" fill="none" stroke="#f7c1b4" stroke-width="1.2"/></svg>
        corinne47@pelvomail.net</span>
      <span class="contact contact--bird"><span class="mark-circle"></span>crvask202</span>
    </div>
  </section>

</div>
</body>
</html>
```